Business card for Internet Marketing Consultant

Simple - need a nice business card design using the logo elements and colors. Keywords: Progressive, professional, stylish, minimalist. Please use the kr as part of the design.

Info for card:

Gareth Pennock
Internet Marketing Strategist
Phone: (555) 813-2064
Email: gareth@korvantareach.com
Address: 2156 N. Halvern Ave., Ste. 118
Marlow Ridge, Arizona 85093

Website: www.korvantareach.com

Business

Sans Serif

```html
<!DOCTYPE html>
<html lang="en">
<head>
<meta charset="utf-8">
<title>Gareth Pennock – Business Card</title>
<link rel="stylesheet" href="https://fonts.googleapis.com/css2?family=Alegreya:wght@400&family=PT+Sans:ital,wght@0,400;0,700;1,400&display=swap">
<style>
  :root {
    --lime: #6cf542;
    --blue: #2d6cf6;
    --teal: #0f7a72;
    --slate: #7d8b8b;
    --ink-shadow: #2a2e2c;
    --paper: #ffffff;
    --page: #ffffff;
  }
  html, body {
    margin: 0;
    width: 1200px;
    height: 1000px;
    overflow: hidden;
    background: var(--page);
  }
  .stage {
    position: relative;
    width: 1200px;
    height: 1000px;
  }
  .card-shadow {
    position: absolute;
    left: 52px;
    top: 176px;
    width: 1111px;
    height: 674px;
    background: var(--ink-shadow);
  }
  .card {
    position: absolute;
    left: 44px;
    top: 168px;
    width: 1111px;
    height: 674px;
    background: var(--paper);
    overflow: hidden;
  }
  .accent-band {
    position: absolute;
    left: 0;
    top: 157px;
    width: 107px;
    height: 517px;
    background: var(--lime);
  }
  .brand-ring {
    position: absolute;
    left: 0;
    top: 0;
  }
  .holder {
    position: absolute;
    left: 121px;
    top: 85px;
    margin: 0;
    font-weight: 400;
  }
  .holder-name {
    display: block;
    font-family: "Alegreya", Georgia, serif;
    font-weight: 400;
    font-size: 42px;
    line-height: 52px;
    color: var(--blue);
  }
  .holder-title {
    display: block;
    font-family: "Alegreya", Georgia, serif;
    font-weight: 400;
    font-size: 29px;
    line-height: 36px;
    color: var(--teal);
  }
  .phone {
    position: absolute;
    left: 121px;
    top: 269px;
    margin: 0;
    font-family: "PT Sans", Arial, sans-serif;
    font-style: italic;
    font-size: 36px;
    color: var(--lime);
  }
  .contact {
    position: absolute;
    left: 121px;
    top: 401px;
    margin: 0;
    font-family: "PT Sans", Arial, sans-serif;
    font-size: 25px;
    line-height: 35px;
    color: var(--blue);
  }
  .contact b { font-weight: 700; }
  .contact .website {
    display: block;
    margin-top: 33px;
    font-weight: 700;
  }
  .brand {
    position: absolute;
    left: 570px;
    top: 250px;
width: 480px;
    text-align: center;
    font-family: "PT Sans", Arial, sans-serif;
  }
  .brand-name {
    display: block;
    font-size: 60px;
    font-weight: 700;
    line-height: 64px;
    color: var(--blue);
  }
  .brand-tagline {
    display: block;
    font-size: 19px;
    font-weight: 400;
    letter-spacing: 3.6px;
    margin-top: 2px;
    color: var(--slate);
  }
</style>
</head>
<body>
<div class="stage">
  <div class="card-shadow"></div>
  <section class="card">
    <div class="accent-band"></div>

    <svg class="brand-ring" width="1111" height="674" viewBox="0 0 1111 674" aria-hidden="true">
      <path fill="var(--blue)" fill-rule="evenodd"
        d="M609 337a295 295 0 1 0 590 0a295 295 0 1 0 -590 0Z
           M764 337a168 168 0 1 0 336 0a168 168 0 1 0 -336 0Z"/>
      <rect x="590" y="245" width="470" height="95" fill="var(--paper)"/>
    </svg>

    <h1 class="holder">
      <span class="holder-name">Gareth Pennock</span>
      <span class="holder-title">Internet Marketing Strategist</span>
    </h1>

    <p class="phone">Phone: (555) 813-2064</p>

    <p class="contact">
      <b>Email:</b> gareth@korvantareach.com<br>
      <b>Address:</b> 2156 N. Halvern Ave., Ste. 118<br>
      Marlow Ridge, Arizona 85093
      <span class="website">Website: www.korvantareach.com</span>
    </p>

    <div class="brand">
      <span class="brand-name">korvantareach</span>
      <span class="brand-tagline">INTERNET MARKETING STRATEGIES</span>
    </div>
  </section>
</div>
</body>
</html>
```